Larkmoor Health- Core Values Graphic for Visual Appeal

I would like a poster that could take these written core values from our organization and create a graphic that we could use for our staff and employees. I would also like to incorporate our branding into this project. Thank you!

Target Market(s)

To helps patients and employees understand the core values of our organization

Industry/Entity Type

Healthcare

Requirements
Must have
• Match our branding
Nice to have
• Please use your creativity!
Should not have
• Overly complex/ busy

```html
<!DOCTYPE html>
<html lang="en">
<head>
<meta charset="utf-8">
<title>Larkmoor Health — Core Values</title>
<link href="https://fonts.googleapis.com/css2?family=Bebas+Neue&family=Quicksand:wght@500;600;700&display=swap" rel="stylesheet">
<style>
  :root {
    --blue: #27a7e1;
    --blue-deep: #1d8fcc;
    --charcoal: #404042;
    --white: #ffffff;
    --shadow-grey: #9d9d9f;
  }
  html, body {
    margin: 0;
    padding: 0;
    width: 1200px;
    height: 992px;
    overflow: hidden;
    background: var(--white);
  }
  .poster {
    position: relative;
    width: 2000px;
    height: 1653px;
    transform: scale(0.6);
    transform-origin: 0 0;
    font-family: "Quicksand", sans-serif;
  }
  .value-path {
    position: absolute;
    left: 990px;
    top: 362px;
    width: 40px;
    height: 928px;
    border-radius: 20px;
    background: linear-gradient(180deg, #d9eef9 0%, var(--blue) 35%, var(--blue) 65%, #d9eef9 100%);
  }
  .connector {
    position: absolute;
    height: 7px;
  }
  .connector--dark { background: var(--charcoal); }
  .connector--blue { background: var(--blue); }

  .value-card {
    position: absolute;
    width: 392px;
    box-sizing: border-box;
    color: var(--white);
  }
  .value-card--blue {
    background: linear-gradient(180deg, var(--blue) 0%, var(--blue) 88%, var(--blue-deep) 100%);
  }
  .value-card--dark { background: var(--charcoal); }
  .value-card--excellence { left: 430px; top: 268px; height: 484px; }
  .value-card--family { left: 1197px; top: 268px; height: 484px; }
  .value-card--service { left: 430px; top: 874px; height: 461px; }
  .value-card--integrity { left: 1197px; top: 874px; height: 461px; }

  .value-title {
    position: absolute;
    top: 23px;
    height: 87px;
    margin: 0;
    background: var(--white);
    border-radius: 12px;
    font-family: "Bebas Neue", sans-serif;
    font-weight: 400;
    font-size: 82px;
    line-height: 94px;
    text-align: center;
    letter-spacing: 1px;
  }
  .value-card--blue .value-title { color: var(--blue); box-shadow: 6px 6px 0 var(--charcoal); }
  .value-card--dark .value-title { color: var(--charcoal); box-shadow: 6px 6px 0 var(--shadow-grey); }
  .value-card--excellence .value-title { left: 23px; width: 349px; }
  .value-card--family .value-title { left: 71px; width: 252px; }
  .value-card--service .value-title { left: 76px; width: 244px; }
  .value-card--integrity .value-title { left: 40px; width: 314px; }

  .value-text {
    position: absolute;
    left: 20px;
    right: 20px;
    top: 124px;
    margin: 0;
    font-size: 20.5px;
    font-weight: 500;
    line-height: 26.8px;
    letter-spacing: 0.3px;
    text-align: center;
    hyphens: auto;
    -webkit-hyphens: auto;
  }
  .brand-mark {
    position: absolute;
    width: 300px;
    margin-left: -150px;
    text-align: center;
  }
  .brand-dot {
    display: block;
    width: 42px;
    height: 42px;
    margin: 0 auto 18px;
    border-radius: 50%;
    background: var(--blue);
  }
  .brand-name {
    font-weight: 700;
    font-size: 30px;
    line-height: 34px;
    white-space: nowrap;
    color: var(--charcoal);
  }
</style>
</head>
<body>
<main class="poster">
  <div class="value-path" role="img" aria-label="Decorative path of dots linking the four values"></div>
  <div class="connector connector--dark" style="left:1030px; top:524px; width:167px;"></div>
  <div class="connector connector--blue" style="left:822px; top:630px; width:168px;"></div>
  <div class="connector connector--blue" style="left:1030px; top:1027px; width:167px;"></div>
  <div class="connector connector--dark" style="left:835px; top:1127px; width:155px;"></div>

  <div class="brand-mark" style="left:1013px; top:108px;"><span class="brand-dot"></span><span class="brand-name">Larkmoor Health</span></div>
  <div class="brand-mark" style="left:272px; top:728px;"><span class="brand-dot"></span><span class="brand-name">Larkmoor Health</span></div>
  <div class="brand-mark" style="left:1728px; top:728px;"><span class="brand-dot"></span><span class="brand-name">Larkmoor Health</span></div>
  <div class="brand-mark" style="left:1013px; top:1385px;"><span class="brand-dot"></span><span class="brand-name">Larkmoor Health</span></div>

  <section class="value-card value-card--blue value-card--excellence">
    <h2 class="value-title">Excellence</h2>
    <p class="value-text">In line with our goal, we aspire not only to alleviate pain but also to inspire patients to become active participants in their well-being. We believe in empowering our patients through education and compassion. Our pursuit of excellence is unwavering, driven by our dedication to continuously improve our services at every level, ensuring that our community receives nothing less than exceptional care.</p>
  </section>

  <section class="value-card value-card--dark value-card--family">
    <h2 class="value-title">Family</h2>
    <p class="value-text">At the heart of our mission is the commitment to provide high-quality, affordable healthcare in a comforting and uplifting family-oriented environment. Just as our community is our extended family, every patient is a cherished member of our healthcare family. We treat each individual with the same care, compassion, and respect we would offer to our own loved ones.</p>
  </section>

  <section class="value-card value-card--dark value-card--service">
    <h2 class="value-title">Service</h2>
    <p class="value-text">Our vision is grounded in the belief that every person possesses the innate potential for true health. We aim to facilitate the body's natural healing response by providing the highest level of service. Our hope for each patient extends beyond healing; we aspire to help you fulfill your life's mission and purpose abundantly, supporting you in your journey to well-being.</p>
  </section>

  <section class="value-card value-card--blue value-card--integrity">
    <h2 class="value-title">Integrity</h2>
    <p class="value-text">In our healthcare team, 'Integrity' is non-negotiable. Our purpose is deeply rooted in ethics, integrity, and professional standards. We operate with the utmost integrity in every aspect of our work, adhering to the highest ethical principles. We understand that trust is the foundation of healthcare, and we are committed to maintaining the trust our community places in us.</p>
  </section>
</main>
</body>
</html>
```